120ml Jar Label — Masculine Cosmetic Foot Balm for Cracked, Hardworking Heels

We need a print-ready wraparound label for a 120ml jar — a brown/amber glass jar with a black metal screw lid (file photo attached).

--DO NOT PUT A BARCODE ON THE LABEL PLEASE--
**PLEASE READ "PIXEL HARBOUR PROJECT BRIEF FINAL.MD" IN ATTACHED FILES IF YOU ARE SUBMITTING A DESIGN.**

The label is 190mm wide × 40mm high.
We need files to be in an .ai format with a 2mm bleed at the end.
Social media handle: @tallowgatenz (facebook, instagram and tiktok)

Tallow Gate is a New Zealand foot-care brand making practical, no-nonsense products for hardworking men whose jobs wreck their feet. Our flagship product, Ridge Mender Balm, helps fix thick, cracked, hardworking skin.

Brand color scheme and overview is all in the brief file. You may add some brand aligned colors outside of the specified hex codes as you see fit to make a great design. Feel free to remove the "Tallow Gate" text from the logo so Tallow Gate is not doubled up on the front of the label

The tone we want: direct, rugged, and credible — like a workwear brand, not a spa brand. Most cracked-heel products on the market lean soft and feminine; we want to stand apart by looking like a serious fix for a real problem, made in New Zealand.

Full legal requirements for New Zealand cosmetic labelling (ingredients, directions, net contents, origin, etc.) are listed in the attached brief document — these are non-negotiable and must stay legible.

Please see the label attached "Label spacing guide" for this project's rough spacing guide. This label is the same size and sits well on the jar. This label doesn't need to be spaced quite as much as the Brisko Label

I want to run the design for a week - I feel 7 days is a good amount of time for designers to see the work, digest the brief and create something remarkable and memorable for Tallow Gate.

Target Market(s)

Working men in New Zealand whose jobs or lifestyle put heavy wear on their feet — tradies, farmers, hospital/shift workers, hunters, and outdoors people. Practical, value-driven buyers rather than luxury skincare shoppers.

Industry/Entity Type

Beauty / Health & Wellness / Cosmetics

Font styles to use
Sans Serif
Other font styles liked:
• Montserrat (bold, headings), Inter (regular, body)

Colors
00AB8E
00BBA5
67D7C9
C6EFE9
E9F9F6
FFC000
F8CF3A
FAE287
FDF2CF
FEFAEE

Requirements
Must have
• All NZ cosmetic labelling requirements from the attached brief (product name, tag line, net contents, ingredients, directions, storage, made in NZ) — legible and complete, not omitted for aesthetics Fits 190mm × 40mm wraparound format for a 120ml brown jar with black lid Uses our existing brand colors: Deep Olive #3C4A34, Bone White #F4EFE6, Terracotta Clay #C1683D, and Warm Grey #4A4540 (exact palette in attached brief) Uses Montserrat (headings) and Inter (body) or close equivalents Incorporates our existing shield-and-wing logo (attached) Brand name and product name clearly readable from a normal shelf/bathroom-cabinet distance
Nice to have
• A style that could extend into a hero/product photo later, similar to the NZ-hills-backdrop look on our website (screenshot attached) — not required for the label itself, just good to keep in mind Original icon work (e.g. a small soak/apply/sock icon set) if it fits the rugged brand feel A design that could work as a small back-label/wraparound split if the front can't fit everything at a readable size
Should not have
• No pastel colors, floral motifs, or delicate script fonts — this should never look like spa/luxury skincare. Don't introduce new brand colors outside the palette provided other than black.

```html
<!DOCTYPE html>
<html lang="en">
<head>
<meta charset="utf-8">
<title>Tallow Gate – Ridge Mender Balm Label</title>
<link href="https://fonts.googleapis.com/css2?family=Barlow+Condensed:wght@700&family=Montserrat:wght@400;500;600;700&display=swap" rel="stylesheet">
<style>
  :root{
    --olive:#4b5a37;
    --olive-dark:#414e30;
    --clay:#d65a2c;
    --clay-soft:#c9542a;
    --bone:#e8e3d6;
    --page:#ffffff;
  }
  *{box-sizing:border-box;margin:0;padding:0}
  html,body{width:1200px;height:670px;overflow:hidden;background:var(--page)}
  body{display:flex;align-items:center;justify-content:center;font-family:"Montserrat",sans-serif;color:var(--bone)}
  .label{
    width:1140px;height:240px;background:var(--clay);
    display:flex;gap:14px;padding:16px 14px;
  }
  .panel{
    flex:1;background:var(--olive);position:relative;
    display:flex;
  }
  /* back panel */
  .panel--back{flex-direction:column;padding:12px 18px 10px;font-size:9.4px;line-height:1.32;font-weight:400}
  .panel--back p{margin-bottom:7px}
  .tag{color:var(--clay);font-weight:600;text-transform:uppercase}
  .origin{display:flex;align-items:center;gap:12px;margin-top:auto}
  .origin-map{width:18px;height:34px;background:var(--bone);opacity:.85;border-radius:8px 3px 10px 2px}
  .origin-text{border-left:1px solid var(--clay);padding-left:10px;font-weight:600;font-size:10.5px;line-height:1.2;text-transform:uppercase}
  /* front panel */
  .panel--front{flex-direction:column;align-items:center;justify-content:center;padding:10px 24px}
  .mark{width:54px;height:54px;border-radius:50%;background:var(--bone);opacity:.9;margin-bottom:8px}
  .brand-row{display:flex;align-items:center;gap:12px;width:100%}
  .rule{flex:1;height:1px;background:var(--clay)}
  .brand{font-weight:600;font-size:19px;letter-spacing:1.5px;text-transform:uppercase;white-space:nowrap}
  .plaque{
    margin:5px 0 8px;border:2px solid var(--clay);border-radius:14px;
    padding:2px 16px;font-family:"Barlow Condensed",sans-serif;font-weight:700;
    font-size:36px;line-height:1;color:var(--clay);text-transform:uppercase;letter-spacing:.5px
  }
  .tagline{font-weight:700;font-size:10px;letter-spacing:.6px;text-transform:uppercase}
  .net-row{display:flex;align-items:center;gap:10px;width:60%;margin-top:4px}
  .net{font-weight:600;font-size:9px}
  /* usage panel */
  .panel--usage{padding:12px 10px 12px 16px}
  .steps{flex:1;display:flex;flex-direction:column;justify-content:space-between}
  .step{display:flex;gap:12px;align-items:center;padding:4px 0}
  .step + .step{border-top:1px solid var(--clay)}
  .step-icon{width:28px;height:40px;border:1.5px solid var(--clay);border-radius:3px;background:var(--olive-dark);flex:none}
  .step-title{color:var(--clay);font-weight:600;font-size:10px;text-transform:uppercase}
  .step-text{font-size:9.4px;line-height:1.3}
  .social{width:34px;display:flex;flex-direction:column;align-items:center;justify-content:center;gap:6px}
  .handle{writing-mode:vertical-rl;transform:rotate(180deg);font-size:11px;font-weight:500;letter-spacing:.5px;padding-bottom:4px;border-bottom:1px solid var(--clay)}
  .dot{width:13px;height:13px;border-radius:50%;background:var(--bone)}
</style>
</head>
<body>
  <main class="label">
    <section class="panel panel--back">
      <p><span class="tag">Directions:</span> Apply generously to clean, dry feet, focusing on heels and thick or cracked areas. For cracked heels, wear our moisture-locking socks overnight. Use daily.</p>
      <p><span class="tag">Ingredients:</span> Shea Butter, Beef Tallow, Beeswax, Grape Seed Oil, Vegetable Glycerin, Lanolin, Panthenol, Gluconolactone &amp; Sodium Benzoate, Manuka Honey, Allantoin, Vitamin E, Tea Tree Essential Oil, Lemon Myrtle Essential Oil, Rosemary Oleoresin Extract</p>
      <p><span class="tag">Storage:</span> Keep out of direct sunlight. Best used within six months of opening.</p>
      <div class="origin">
        <div class="origin-map" role="img" aria-label="Outline map of New Zealand"></div>
        <div class="origin-text">Made in<br>New Zealand</div>
      </div>
    </section>

    <section class="panel panel--front">
      <div class="mark" role="img" aria-label="Tallow Gate brand mark"></div>
      <div class="brand-row"><span class="rule"></span><h1 class="brand">Tallow Gate</h1><span class="rule"></span></div>
      <h2 class="plaque">Ridge Mender Balm</h2>
      <div class="tagline">For hardworking soles</div>
      <div class="net-row"><span class="rule"></span><span class="net">120ML</span><span class="rule"></span></div>
    </section>

    <section class="panel panel--usage">
      <div class="steps">
        <div class="step">
          <div class="step-icon" role="img" aria-label="Icon of a hand applying balm from a jar"></div>
          <div><div class="step-title">Apply</div><div class="step-text">Massage daily into clean,<br>dry sore heels.</div></div>
        </div>
        <div class="step">
          <div class="step-icon" role="img" aria-label="Icon of a sock"></div>
          <div><div class="step-title">Overnight</div><div class="step-text">Wear socks overnight to<br>lock in moisture.</div></div>
        </div>
        <div class="step">
          <div class="step-icon" role="img" aria-label="Icon of a restored foot with sparkles"></div>
          <div><div class="step-title">Restore</div><div class="step-text">Heels ready to go,<br>day after day.</div></div>
        </div>
      </div>
      <div class="social">
        <span class="handle">@tallowgatenz</span>
        <span class="dot"></span><span class="dot"></span><span class="dot"></span>
      </div>
    </section>
  </main>
</body>
</html>
```